'Brantley Electrical' web design

I need a web design for an electrical/electrician company based in sydney called brantley electrical. The logo design and business card design have been uploaded to be used on the web design. I want the design to be very modern and clean. I want the sector designs on the business card, i.e "residential", "commercial" etc, to be fleshed out on the front page. Base those sector designs off the business card but try to make them more minimal and modern to suit the website. Contact details are also on the business card. Try to suit the colour scheme of the logo. The sector designs should be up the top and linked so when clicked it will scroll down the website to brief descriptions of the work the company does in those sectors. I want the website to mainly attract builders, insurance companies and the commercial sector. I want the website to look unique. Custom graphics would be nice to make the website standout. I don't want the website to look like generic.

Target Market(s)

Builders, commercial sector, home owners

Industry/Entity Type

Electrical/Construction

Coding

Coded - Design and coding required

Number of Pages Required

3 page

Requirements
Must have
• Modern design
Nice to have
• Custom graphics that make the website unique

```html
<!DOCTYPE html>
<html lang="en">
<head>
<meta charset="utf-8">
<title>Brantley Electrical</title>
<link rel="stylesheet" href="https://fonts.googleapis.com/css2?family=Montserrat:wght@400;500;600&family=Poppins:ital,wght@0,500;0,600;1,600&display=swap">
<style>
:root{
  --blue:#0f5bb3;
  --blue-deep:#0b4f9e;
  --orange:#f08550;
  --orange-dark:#d96a34;
  --ink:#3a3a3a;
  --footer:#2b2b2b;
  --faint:#e9eef5;
  --white:#ffffff;
}
*{margin:0;padding:0;box-sizing:border-box}
html,body{width:1200px;height:3432px;overflow:hidden;background:var(--white)}
body{position:relative;font-family:'Montserrat',sans-serif;color:var(--ink)}
.abs{position:absolute}

/* header */
.brand{left:112px;top:22px;display:flex;align-items:center;gap:10px}
.brand-mark{width:26px;height:26px;background:var(--blue)}
.brand-name{font-family:'Poppins',sans-serif;font-weight:600;font-size:25px;color:var(--blue);text-transform:uppercase}
.contact-chip{top:18px;display:flex;align-items:center;gap:12px}
.chip-icon{width:38px;height:38px;border-radius:50%;background:linear-gradient(135deg,var(--blue),var(--orange));display:flex;align-items:center;justify-content:center}
.chip-label{font-size:13px;color:#555}
.chip-value{font-family:'Poppins',sans-serif;font-weight:600;font-size:17px;color:var(--blue);line-height:1.2}

.nav{left:0;top:76px;width:1200px;height:40px;background:var(--orange);display:flex;align-items:center;padding-left:146px}
.nav a{color:var(--white);text-decoration:none;font-size:15px;padding:0 32px;border-left:1px solid rgba(255,255,255,.6);line-height:14px}
.nav a:first-child{border-left:none;padding-left:0;font-weight:600}

/* hero */
.hero{left:0;top:116px;width:1200px;height:471px;overflow:hidden}
.hero-photo{position:absolute;inset:0;background:linear-gradient(120deg,#cfd3d6 30%,#b7b1a4 55%,#d9d96a 80%,#8a8f94)}
.hero-panel{position:absolute;inset:0;background:var(--blue);clip-path:polygon(0 0,522px 0,606px 100%,0 100%)}
.hero-copy{position:absolute;left:112px;top:92px;width:380px;color:var(--white)}
.hero-copy .eyebrow{font-family:'Poppins',sans-serif;font-weight:500;font-size:27px}
.hero-copy h1{font-family:'Poppins',sans-serif;font-weight:500;font-size:42px;margin-top:6px;letter-spacing:.5px}
.hero-copy p{font-size:15.5px;line-height:27.5px;margin-top:22px}
.btn{display:inline-block;background:var(--orange);color:var(--white);font-weight:600;font-size:15px;padding:10px 16px;box-shadow:4px 4px 0 var(--orange-dark);text-decoration:none}
.hero-copy .btn{margin-top:36px}

/* sectors */
.sector-photo{height:436px;width:567px}
.sector-card{width:496px;height:343px;background:var(--white);box-shadow:0 10px 40px rgba(0,0,0,.08);padding:52px 38px 0}
.sector-card h2{font-family:'Poppins',sans-serif;font-style:italic;font-weight:600;font-size:24px;color:var(--blue);display:flex;align-items:center;gap:8px}
.sector-card p{font-size:15px;line-height:26px;text-align:justify;margin-top:18px}
.sector-card p+p{margin-top:8px}
.sector-card .arrow{margin-top:28px;display:block}
.rule{display:inline-block;width:26px}
.sector-word{font-family:'Poppins',sans-serif;font-style:italic;font-weight:600;font-size:58px;color:var(--faint);writing-mode:vertical-rl;white-space:nowrap;letter-spacing:1px}
.word-right{right:-6px;transform:rotate(180deg)}
.word-left{left:-6px}

/* about */
.about{left:0;top:2724px;width:1200px;height:365px;background:linear-gradient(90deg,var(--blue-deep),var(--blue));text-align:center;color:var(--white)}
.about h2{font-family:'Poppins',sans-serif;font-style:italic;font-weight:600;font-size:30px;margin-top:74px;display:flex;justify-content:center;align-items:center;gap:20px}
.about p{width:850px;margin:22px auto 0;font-size:15.5px;line-height:27.5px}
.about .btn{margin-top:30px}

/* footer */
.footer{left:0;top:3089px;width:1200px;height:343px;background:var(--footer);color:var(--white)}
.foot-brand{left:140px;top:86px;width:220px;text-align:center}
.foot-brand .brand-name{color:var(--orange);font-size:24px}
.foot-brand .brand-mark{width:30px;height:30px;background:var(--orange);margin:0 auto 14px}
.socials{left:150px;top:224px;display:flex;gap:28px}
.socials span{width:22px;height:22px;border-radius:50%;background:var(--white)}
.foot-col h3{font-family:'Poppins',sans-serif;font-weight:500;font-size:18px;margin-bottom:14px}
.foot-col li{list-style:none;font-size:15px;line-height:30px;color:#e6e6e6}
.contact-row{display:flex;gap:14px;font-size:15px;line-height:30px;margin-bottom:16px}
.contact-row svg{margin-top:8px;flex:none}
.copyright{left:0;top:308px;width:1200px;text-align:center;font-size:14px;color:#e6e6e6}
</style>
</head>
<body>

<header>
  <div class="abs brand"><span class="brand-mark"></span><span class="brand-name">Brantley Electrical</span></div>
  <div class="abs contact-chip" style="left:638px">
    <span class="chip-icon"><svg width="18" height="14" viewBox="0 0 18 14"><rect x="1" y="1" width="16" height="12" fill="none" stroke="#fff" stroke-width="1.6"/><path d="M1 1l8 7 8-7" fill="none" stroke="#fff" stroke-width="1.6"/></svg></span>
    <div><div class="chip-label">Mail Us</div><div class="chip-value">hello@brantleyelectrical.com.au</div></div>
  </div>
  <div class="abs contact-chip" style="left:970px">
    <span class="chip-icon"><svg width="16" height="16" viewBox="0 0 24 24"><path d="M6.6 10.8a15 15 0 0 0 6.6 6.6l2.2-2.2a1 1 0 0 1 1-.25 11.4 11.4 0 0 0 3.6.57 1 1 0 0 1 1 1V20a1 1 0 0 1-1 1A17 17 0 0 1 3 4a1 1 0 0 1 1-1h3.5a1 1 0 0 1 1 1c0 1.25.2 2.45.57 3.57a1 1 0 0 1-.25 1z" fill="#fff"/></svg></span>
    <div><div class="chip-label">Get In Touch</div><div class="chip-value">+0412 305 918</div></div>
  </div>
  <nav class="abs nav">
    <a href="#">Home</a><a href="#">About Us</a><a href="#">Commercial</a><a href="#">Construction</a><a href="#">Industrial</a><a href="#">Residential</a><a href="#">Contact Us</a>
  </nav>
</header>

<section class="abs hero">
  <div class="hero-photo" role="img" aria-label="Smiling electrician in hard hat and safety vest working on a wiring cabinet"></div>
  <div class="hero-panel"></div>
  <div class="hero-copy">
    <div class="eyebrow">Welcome To</div>
    <h1>BRANTLEY ELECTRICAL</h1>
    <p>Lorem ipsum dolor sit amet, consectetur adipiscing elit, sed do eiusmod tempor incididunt ut labore et dolore magna aliqua uis ipsum suspendisse.</p>
    <a class="btn" href="#">Get Started</a>
  </div>
</section>

<!-- Commercial -->
<div class="abs sector-word word-right" style="top:670px">COMMERCIAL</div>
<div class="abs sector-photo" style="left:0;top:658px;background:linear-gradient(120deg,#9aa3ab,#c9cdd0 45%,#e2773a 75%,#b9bec2)" role="img" aria-label="Electrician in orange overalls testing a switchboard"></div>
<article class="abs sector-card" style="left:509px;top:704px">
  <h2>COMMERCIAL SERVICES <svg class="rule" width="26" height="12"><path d="M2 3h24M0 6h24M2 9h24" stroke="#f08550" stroke-width="1.5"/></svg></h2>
  <p>Lorem ipsum dolor sit amet, consectetur adipiscing elit, sed do eiusmod tempor incididunt ut labore et dolore magna aliqua. Quis ipsum suspendisse ultrices gravida. Risus commodo viverra maecenas.</p>
  <p>Quis ipsum suspendisse ultrices gravida. Risus commodo viverra maecenas.</p>
  <svg class="arrow" width="50" height="14"><path d="M0 7h48M41 1l7 6-7 6" fill="none" stroke="#f08550" stroke-width="1.6"/></svg>
</article>

<!-- Construction -->
<div class="abs sector-word word-left" style="top:1155px">CONSTRUCTION</div>
<div class="abs sector-photo" style="left:633px;top:1180px;background:linear-gradient(160deg,#c79a63,#e2c08e 40%,#a97848 75%,#d8c63a)" role="img" aria-label="Electrician on a ladder wiring the timber frame of a new building"></div>
<article class="abs sector-card" style="left:191px;top:1227px">
  <h2>CONSTRUCTION SERVICES <svg class="rule" width="26" height="12"><path d="M2 3h24M0 6h24M2 9h24" stroke="#f08550" stroke-width="1.5"/></svg></h2>
  <p>Lorem ipsum dolor sit amet, consectetur adipiscing elit, sed do eiusmod tempor incididunt ut labore et dolore magna aliqua. Quis ipsum suspendisse ultrices gravida. Risus commodo viverra maecenas.</p>
  <p>Quis ipsum suspendisse ultrices gravida. Risus commodo viverra maecenas.</p>
  <svg class="arrow" width="50" height="14"><path d="M0 7h48M41 1l7 6-7 6" fill="none" stroke="#f08550" stroke-width="1.6"/></svg>
</article>

<!-- Industrial -->
<div class="abs sector-word word-right" style="top:1752px">INDUSTRIAL</div>
<div class="abs sector-photo" style="left:0;top:1712px;background:linear-gradient(120deg,#d7dde2,#aab2b8 45%,#f29a3a 65%,#c8cdd1)" role="img" aria-label="Technician in hi-vis vest working on an outdoor industrial control cabinet"></div>
<article class="abs sector-card" style="left:509px;top:1758px">
  <h2>INDUSTRIAL SERVICES <svg class="rule" width="26" height="12"><path d="M2 3h24M0 6h24M2 9h24" stroke="#f08550" stroke-width="1.5"/></svg></h2>
  <p>Lorem ipsum dolor sit amet, consectetur adipiscing elit, sed do eiusmod tempor incididunt ut labore et dolore magna aliqua. Quis ipsum suspendisse ultrices gravida. Risus commodo viverra maecenas.</p>
  <p>Quis ipsum suspendisse ultrices gravida. Risus commodo viverra maecenas.</p>
  <svg class="arrow" width="50" height="14"><path d="M0 7h48M41 1l7 6-7 6" fill="none" stroke="#f08550" stroke-width="1.6"/></svg>
</article>

<!-- Residential -->
<div class="abs sector-word word-left" style="top:2262px">RESIDENTAL</div>
<div class="abs sector-photo" style="left:633px;top:2221px;background:linear-gradient(140deg,#e8eaec,#c9d3dc 45%,#c98a3e 70%,#dfe3e6)" role="img" aria-label="Electrician in gloves pulling cables from a wall"></div>
<article class="abs sector-card" style="left:191px;top:2267px">
  <h2>RESIDENTAL SERVICES <svg class="rule" width="26" height="12"><path d="M2 3h24M0 6h24M2 9h24" stroke="#f08550" stroke-width="1.5"/></svg></h2>
  <p>Lorem ipsum dolor sit amet, consectetur adipiscing elit, sed do eiusmod tempor incididunt ut labore et dolore magna aliqua. Quis ipsum suspendisse ultrices gravida. Risus commodo viverra maecenas.</p>
  <p>Quis ipsum suspendisse ultrices gravida. Risus commodo viverra maecenas.</p>
  <svg class="arrow" width="50" height="14"><path d="M0 7h48M41 1l7 6-7 6" fill="none" stroke="#f08550" stroke-width="1.6"/></svg>
</article>

<section class="abs about">
  <h2><svg width="26" height="12"><path d="M2 3h24M0 6h24M2 9h24" stroke="#f08550" stroke-width="1.5"/></svg>ABOUT US<svg width="26" height="12"><path d="M2 3h24M0 6h24M2 9h24" stroke="#f08550" stroke-width="1.5"/></svg></h2>
  <p>Et harum quidem rerum facilis est et expedita distinctio. Nam libero tempore, cum soluta nobis est eligendi optio cumque nihil impedit quo minus id quod maxime placeat facere possimus, omnis voluptas assumenda est, omnis dolor repellendus. Temporibus autem quibusdam et aut officiis debitis aut rerum necessitatibus saepe eveniet ut et voluptates repudiandae sint et molestiae non recusandae.</p>
  <a class="btn" href="#">Get Started</a>
</section>

<footer class="abs footer">
  <div class="abs foot-brand"><span class="brand-mark" style="display:block"></span><span class="brand-name">Brantley Electrical</span></div>
  <div class="abs socials"><span></span><span></span><span></span><span></span></div>
  <div class="abs foot-col" style="left:475px;top:70px">
    <h3>Contact</h3>
    <div class="contact-row"><svg width="12" height="16" viewBox="0 0 12 16"><path d="M6 0a6 6 0 0 0-6 6c0 4.5 6 10 6 10s6-5.5 6-10a6 6 0 0 0-6-6zm0 8.5A2.5 2.5 0 1 1 6 3.5a2.5 2.5 0 0 1 0 5z" fill="#f08550"/></svg><div>Brantley Electrical,<br>Address Comes Here</div></div>
    <div class="contact-row"><svg width="14" height="14" viewBox="0 0 24 24"><path d="M6.6 10.8a15 15 0 0 0 6.6 6.6l2.2-2.2a1 1 0 0 1 1-.25 11.4 11.4 0 0 0 3.6.57 1 1 0 0 1 1 1V20a1 1 0 0 1-1 1A17 17 0 0 1 3 4a1 1 0 0 1 1-1h3.5a1 1 0 0 1 1 1c0 1.25.2 2.45.57 3.57a1 1 0 0 1-.25 1z" fill="#f08550"/></svg><div>+0412 305 918</div></div>
    <div class="contact-row"><svg width="14" height="11" viewBox="0 0 14 11"><rect width="14" height="11" fill="#f08550"/><path d="M0 0l7 6 7-6" fill="none" stroke="#2b2b2b" stroke-width="1.3"/></svg><div>hello@brantleyelectrical.com.au</div></div>
  </div>
  <div class="abs foot-col" style="left:758px;top:70px">
    <h3>Quick Links</h3>
    <ul><li>House</li><li>About</li><li>Terms &amp; Conditions</li><li>Privacy Policy</li><li>Contact Us</li></ul>
  </div>
  <div class="abs foot-col" style="left:946px;top:70px">
    <h3>Our Services</h3>
    <ul><li>Commercial</li><li>Construction</li><li>Industrial</li><li>Residential</li></ul>
  </div>
  <div class="abs copyright">2023 Brantley Electrical.&nbsp; Alle rechten voorbehouden.</div>
</footer>

</body>
</html>
```